Stationery Design Project

Need stationery based on logo

Stationery should include:

Letterhead-should include logo at the top, and contact info at the bottom
Envelope should include mailing address  at top left corner (Corvath Tutoring Services, 4867 Brisk...)
PPT slide should include Logo only
Cover page should just include logo

Requirements
Must have
• Based on logo

```html
<!DOCTYPE html>
<html lang="en">
<head>
<meta charset="utf-8">
<title>Corvath Tutoring Services – Stationery</title>
<link rel="stylesheet" href="https://fonts.googleapis.com/css2?family=Libre+Baskerville&family=Source+Sans+3:wght@400&display=swap">
<style>
  :root {
    --backdrop: #e4e4e4;
    --paper: #ffffff;
    --teal: #00a39a;
    --ink: #3f3f3f;
    --ink-soft: #5a5a5a;
  }
  * { margin: 0; padding: 0; box-sizing: border-box; }
  html, body {
    width: 1200px;
    height: 907px;
    overflow: hidden;
    background: var(--backdrop);
  }
  .canvas {
    position: relative;
    width: 1200px;
    height: 907px;
  }
  .cover-page,
  .letterhead {
    position: absolute;
    left: 323px;
    width: 564px;
    background: var(--paper);
    overflow: hidden;
  }
  .cover-page { top: 45px; height: 397px; }
  .cover-band {
    position: absolute;
    left: 0; right: 0;
    top: 208px; bottom: 0;
    background: var(--teal);
  }
  .brand-name {
    position: absolute;
    left: 0; right: 0;
    text-align: center;
    font-family: "Libre Baskerville", Georgia, serif;
    font-weight: 400;
    color: var(--ink);
    white-space: nowrap;
  }
  .cover-page .brand-name {
    top: 170px;
    font-size: 21px;
    letter-spacing: 1.5px;
  }
  .letterhead { top: 471px; height: 397px; }
  .letterhead .brand-name {
    top: 48px;
    font-size: 12px;
    letter-spacing: 1px;
  }
  .brand-mark {
    display: inline-block;
    width: 9px; height: 9px;
    background: var(--teal);
    margin-right: 8px;
    vertical-align: 1px;
  }
  .cover-page .brand-mark { width: 14px; height: 14px; margin-right: 10px; vertical-align: 2px; }
  .letterhead-contact {
    position: absolute;
    left: 0; right: 0;
    bottom: 12px;
    text-align: center;
    font-family: "Source Sans 3", Arial, sans-serif;
    font-size: 7.5px;
    color: var(--ink-soft);
    white-space: nowrap;
  }
</style>
</head>
<body>
<main class="canvas">
  <section class="cover-page" aria-label="Cover page">
    <div class="cover-band"></div>
    <p class="brand-name"><span class="brand-mark"></span>Corvath Tutoring Services</p>
  </section>

  <section class="letterhead" aria-label="Letterhead">
    <p class="brand-name"><span class="brand-mark"></span>Corvath Tutoring Services</p>
    <p class="letterhead-contact">4867 Brisk Lane • Alder Falls, CA 95720 • 650-555-0142 • hello@corvathtutoring.com</p>
  </section>
</main>
</body>
</html>
```